Business Card for premium dental clinic

We are a premium dental clinic based in Brasov, Romania with more than 15 year on the market, providing quality dental treatment made by a team of more specialized dentists, working with modern equipment as a solution to beautiful and healthy teeth.

Our current logo for the clinic use 2 square with colors black and gold - dr Corbescu - studio, using family fonts Bodoni, Myriad Pro and Segoe Print.
Depending on the printing we used some gold CMYK background or gold foil picture background or a gold gradient.
We want a business card:
- eye catching business card
- distinguished business card
- premium design
- to keep the color scheme of black and gold
- to attract the customers to spent time reading the information
- modern concept

```html
<!DOCTYPE html>
<html lang="en">
<head>
<meta charset="utf-8">
<title>Lumora Dental – Business Card</title>
<link rel="stylesheet" href="https://fonts.googleapis.com/css2?family=Montserrat:wght@400;500;700&display=swap">
<style>
  :root {
    --backdrop: #e8e6e2;
    --card: #323234;
    --gold: #d8ab2e;
    --gold-edge: #e2c048;
    --white: #ffffff;
    --muted-white: #e9e9e9;
  }
  * { box-sizing: border-box; margin: 0; padding: 0; }
  html, body {
    width: 1200px;
    height: 800px;
    overflow: hidden;
    background: var(--backdrop);
    font-family: "Montserrat", Arial, sans-serif;
  }
  .sheet {
    width: 1200px;
    height: 800px;
    display: flex;
    align-items: center;
    justify-content: center;
    gap: 40px;
  }
  .card {
    position: relative;
    width: 540px;
    height: 310px;
    background: var(--card);
    border-left: 2px solid var(--gold-edge);
    border-bottom: 2px solid var(--gold-edge);
    box-shadow: 0 6px 18px rgba(0, 0, 0, 0.18);
  }

  /* Front */
  .card-front {
    display: flex;
    align-items: center;
    justify-content: center;
  }
  .brand-name {
    color: var(--gold);
    font-weight: 500;
    letter-spacing: 0.5px;
    white-space: nowrap;
  }
  .card-front .brand-name { font-size: 44px; }

  /* Back */
  .card-back {
    display: flex;
    align-items: center;
    padding: 0 0 0 34px;
  }
  .card-back .brand-name {
    font-size: 26px;
    width: 210px;
    text-align: center;
  }
  .divider {
    width: 1px;
    height: 130px;
    background: var(--muted-white);
    margin: 0 24px 0 18px;
  }
  .details { color: var(--gold); font-size: 13px; line-height: 1.35; }
  .person-name { color: var(--white); font-weight: 700; font-size: 20px; line-height: 1.1; }
  .person-role { font-size: 13px; margin-bottom: 10px; }
  .address { margin-bottom: 10px; }
  .contact-list { list-style: none; }
  .contact-list li {
    display: flex;
    align-items: center;
    gap: 8px;
    margin-bottom: 3px;
  }
  .contact-list svg { width: 13px; height: 13px; flex: none; fill: var(--white); }
  .contact-list .no-icon { width: 13px; flex: none; }
</style>
</head>
<body>
  <main class="sheet">
    <section class="card card-front" aria-label="Card front">
      <span class="brand-name">Lumora Dental</span>
    </section>

    <section class="card card-back" aria-label="Card back">
      <span class="brand-name">Lumora Dental</span>
      <div class="divider"></div>
      <div class="details">
        <p class="person-name">Andrei Moraru</p>
        <p class="person-role">Manager</p>
        <p class="address">Your address, city<br>state, ZIP 0000</p>
        <ul class="contact-list">
          <li>
            <svg viewBox="0 0 24 24" aria-hidden="true"><path d="M6.6 10.8a15.1 15.1 0 0 0 6.6 6.6l2.2-2.2a1 1 0 0 1 1-.25 11.4 11.4 0 0 0 3.6.57 1 1 0 0 1 1 1V20a1 1 0 0 1-1 1A17 17 0 0 1 3 4a1 1 0 0 1 1-1h3.5a1 1 0 0 1 1 1c0 1.25.2 2.45.57 3.57a1 1 0 0 1-.25 1z"/></svg>
            <span>123-456-7800</span>
          </li>
          <li>
            <svg viewBox="0 0 24 24" aria-hidden="true"><path d="M2 5h20v14H2z M4 7v.5l8 5 8-5V7l-8 5z" fill-rule="evenodd"/></svg>
            <span>contact@lumoradental.ro</span>
          </li>
          <li>
            <svg viewBox="0 0 24 24" aria-hidden="true"><path d="M12 2a10 10 0 1 0 0 20 10 10 0 0 0 0-20zm0 2a8 8 0 0 1 2.9.55L13 7H9L7.6 5.3A8 8 0 0 1 12 4zm-6 3.6L8 10l-1 4-2.6 1.2A8 8 0 0 1 6 7.6zM10 19.7 11 16h3l1.6 3.1a8 8 0 0 1-5.6.6zm8-2.4-1.6-3.3 1.6-4 1.7-.5a8 8 0 0 1-1.7 7.8z"/></svg>
            <span>www.lumoradental.ro</span>
          </li>
        </ul>
      </div>
    </section>
  </main>
</body>
</html>
```